Business Cards for Tandrix Office
Simplifying your policy needs
Bright & Fun-filled
Gordon Lavelle
CEO
8 Carrow Lane Unit #342 Marblehead, MA 01862
glavelle@tandrixoffice.net
www.tandrixoffice.net
Please view our site at www.tandrixoffice.net to understand what we are doing. we have created on online solution to help Credit Union manage and distribute their policies and procedures. Looking at rounded corners and 14pt stock paper
The URL of the site is VERY important since everything is online

```html
<!DOCTYPE html>
<html lang="en">
<head>
<meta charset="utf-8">
<title>Tandrix Office — Stationery</title>
<link href="https://fonts.googleapis.com/css2?family=Open+Sans:wght@400;600;800&display=swap" rel="stylesheet">
<style>
  :root{
    --blue:#1f7fd0;
    --blue-dark:#1565b0;
    --blue-light:#4aa3ea;
    --green:#7cc242;
    --ink:#4a4a4a;
    --muted:#8a8a8a;
    --paper:#ffffff;
    --backdrop:#e9ebee;
  }
  *{box-sizing:border-box;margin:0;padding:0}
  html,body{width:1200px;height:897px;overflow:hidden}
  body{background:var(--backdrop);font-family:"Open Sans",Arial,sans-serif;color:var(--ink);position:relative}
  .sheet{position:absolute;background:var(--paper);box-shadow:0 6px 18px rgba(0,0,0,.15);overflow:hidden}

  .brand{display:flex;align-items:center;gap:8px}
  .brand-dot{width:20px;height:20px;border-radius:50%;background:var(--green);flex:none}
  .brand-name{font-weight:800;color:var(--blue);font-size:18px;line-height:1;letter-spacing:-.2px}

  .band{position:absolute;left:0;right:0;bottom:0;background:linear-gradient(90deg,var(--blue-dark),var(--blue-light));border-top:4px solid var(--green);color:#fff;display:flex;align-items:center;justify-content:center}

  /* business card front */
  .card-front{left:40px;top:40px;width:380px;height:217px;border-radius:14px}
  .card-front .brand{position:absolute;left:24px;top:46px}
  .card-front .person{position:absolute;right:22px;top:22px;text-align:left;width:170px}
  .person-name{color:var(--green);font-weight:600;font-size:14px}
  .person-role{font-size:10px;color:var(--muted);margin-bottom:6px}
  .person-line{font-size:9px;line-height:1.45;color:var(--ink)}
  .card-front .band{height:48px;font-size:12px;font-weight:600;letter-spacing:.6px}

  /* business card back */
  .card-back{left:40px;top:287px;width:380px;height:217px;border-radius:14px;background:radial-gradient(circle at 40% 40%,var(--blue-light),var(--blue-dark));color:#fff;display:flex;flex-direction:column;align-items:center;justify-content:center;gap:14px}
  .card-back .brand-name{color:#fff;font-size:24px}
  .card-back .brand-dot{background:#fff;width:24px;height:24px}
  .card-back .url{font-size:15px;font-weight:600;letter-spacing:.4px}

  /* envelope front */
  .envelope-front{left:40px;top:544px;width:380px;height:190px}
  .envelope-front .brand{position:absolute;left:22px;bottom:56px}
  .envelope-front .brand-name{font-size:15px}
  .envelope-front .brand-dot{width:16px;height:16px}
  .envelope-front .band{height:26px}

  /* envelope back */
  .envelope-back{left:920px;top:40px;width:240px;height:130px}
  .envelope-back svg{position:absolute;inset:0}

  /* letterhead */
  .letterhead{left:460px;top:40px;width:420px;height:594px;padding:32px 34px}
  .letterhead .head{display:flex;justify-content:space-between;align-items:flex-start;margin-bottom:34px}
  .letterhead .contact{font-size:8px;line-height:1.5;color:var(--muted);text-align:left}
  .letter-body{font-size:9px;line-height:1.6;color:var(--ink)}
  .letter-body p{margin-bottom:10px}
  .signature-name{color:var(--green);font-weight:600;margin-top:22px}
  .letterhead .band{height:34px;font-size:11px;font-weight:600;letter-spacing:.5px}
</style>
</head>
<body>

  <section class="sheet card-front" aria-label="Business card front">
    <div class="brand"><span class="brand-dot"></span><span class="brand-name">Tandrix Office</span></div>
    <div class="person">
      <div class="person-name">Gordon Lavelle</div>
      <div class="person-role">CEO</div>
      <div class="person-line">8 Carrow Lane Unit #342</div>
      <div class="person-line">Marblehead, MA 01862</div>
      <div class="person-line">T (781) 555-0142</div>
      <div class="person-line">glavelle@tandrixoffice.net</div>
      <div class="person-line">www.tandrixoffice.net</div>
    </div>
    <div class="band">Simplifying your policy needs</div>
  </section>

  <section class="sheet card-back" aria-label="Business card back">
    <div class="brand"><span class="brand-dot"></span><span class="brand-name">Tandrix Office</span></div>
    <div class="url">www.tandrixoffice.net</div>
  </section>

  <section class="sheet envelope-front" aria-label="Envelope front">
    <div class="brand"><span class="brand-dot"></span><span class="brand-name">Tandrix Office</span></div>
    <div class="band"></div>
  </section>

  <section class="sheet envelope-back" aria-label="Envelope back">
    <svg viewBox="0 0 240 130" width="240" height="130">
      <defs>
        <linearGradient id="flapBlue" x1="0" x2="1">
          <stop offset="0" stop-color="#1565b0"/>
          <stop offset="1" stop-color="#4aa3ea"/>
        </linearGradient>
      </defs>
      <polygon points="0,0 240,0 120,64" fill="url(#flapBlue)"/>
      <polyline points="0,0 120,64 240,0" fill="none" stroke="#7cc242" stroke-width="3"/>
      <circle cx="120" cy="34" r="8" fill="#ffffff"/>
    </svg>
  </section>

  <section class="sheet letterhead" aria-label="Letterhead">
    <div class="head">
      <div class="brand"><span class="brand-dot"></span><span class="brand-name">Tandrix Office</span></div>
      <div class="contact">
        8 Carrow Lane Unit #342<br>
        Marblehead, MA 01862<br>
        T (781) 555-0142<br>
        glavelle@tandrixoffice.net
      </div>
    </div>
    <div class="letter-body">
      <p>Dear Credit Union Partner,</p>
      <p>Thank you for choosing our online service to manage and share your policies and procedures. Every document your team needs is now kept in one secure place, ready to update and distribute in minutes.</p>
      <p>Our support staff is happy to walk you through each step. Please reach out with any question at all.</p>
      <p>Kind regards,</p>
      <div class="signature-name">Gordon Lavelle</div>
      <div>CEO</div>
    </div>
    <div class="band">www.tandrixoffice.net</div>
  </section>

</body>
</html>
```